Broschüre für gemeinnütziges Unternehmen in den Bereichen Kunst, Kultur, Genuss und Heimatpflege
Guten Morgen Tilda am Mühlbach, lieben Dank für die schöne, flexible und rasche Arbeit! Top Kontakt! Habe den Erhalt der Daten eben bestätigt. Viele Grüße Harald Wolting
Zielgruppe
Wir kümmern uns als gemeinnützige GmbH in der Stadt Lindenhain um alles, was mit Kunst, Kultur, Genuss und Heimatpflege zu tun hat. Dafür erstellen wir immer zum Jahresende (Ende Oktober, Anfang November) eine Broschüre mit unserem Programm für das Folgejahr. Unsere Zielgruppe sind Bürgerinnen und Bürger aus dem ganzen Kreisgebiet und darüber hinaus, Altersstruktur 30plus. Der neue Look der Broschüre sollte hochwertig und modern sein.
Aufgabenstellung
Die Broschüre hat eine Klammerheftung und wird ca. 64 Seiten umfassen.
Format: 14,8 x 14,8 cm
In der Anlage an diese Anfrage befinden sich Fotos von Musterseiten, wobei 'Titelseite' die aktuelle Titelseite zeigt, 'Foto 1' eine bisherige Innenseite zeigt, 'Seite 2' und 'Seite 3/4' zeigen Musterseiten, die verdeutlichen sollen, in welche Moderene und reduzierte Richtung es gehen soll. 'Foto Übersicht' zeigt eine chronologische Übersicht. Die Broschüre soll also einen moderneren Look bekommen, gerne auch mal mit einer Doppelseite. Die Musterseiten 2 und 3/4 sind allerdings aus einer Broschüre einer Nachbarkommune, unser Heft sollte sich also davon unterscheiden.
Wichtig sind immer pro Innenseite (oder Innen-Doppelseite): Ein Foto, Titel (z.B. 'Malvina', Genre 'Live-Musik' oder 'Musik und Songnächte', Eckdaten (Datum, Uhrzeit, Location, weitere Infos), Text.
Uns wäre mit einer schön gestalteten Titelseite, sowie schön gestalteten Muster-Innenseiten (je eine Einzelseite, eine Doppelseite, eine Seite mit tabellarischer Übersicht) sehr geholfen. Wir würden dann mit der Vorlage arbeiten und die anderen Seiten 'bauen'. Wäre das ein gangbarer Weg?
Für die Titelseite kann sehr gerne Stockmaterial verwendet werden, für den Innenteil stellen wir die Fotos.
Vielleicht können Musterseiten zu 'Malvina' ('Foto 1') gestaltet werden? Das passenden Foto hängt an, es kann mit Blindtext gearbeitet werden.
Ich freue mich über ein rasches Angebot.
Ihr
Harald Wolting

```html
<!DOCTYPE html>
<html lang="de">
<head>
<meta charset="utf-8">
<title>Lindenhain Veranstaltungen 2024 – Broschürenentwurf</title>
<link href="https://fonts.googleapis.com/css2?family=Poiret+One&family=Quicksand:wght@300;400&display=swap" rel="stylesheet">
<style>
  :root{
    --teal:#1f8597;
    --ink:#111;
    --black:#000;
    --white:#fff;
    --rule:#cfcfcf;
    --violet:#3a1f7a;
  }
  *{box-sizing:border-box;margin:0;padding:0}
  html,body{width:848px;height:1200px;overflow:hidden;background:var(--white)}
  body{position:relative;font-family:"Quicksand",sans-serif;font-weight:300;color:var(--ink)}
  .display{font-family:"Poiret One","Quicksand",sans-serif;font-weight:400}
  .font-note{position:absolute;left:51px;top:16px;font-size:21px;letter-spacing:1px}
  .font-note small{font-size:14px}
  .panel{position:absolute;overflow:hidden}
  .abs{position:absolute}
  .teal{color:var(--teal)}
  .white{color:var(--white)}
  .bar{position:absolute;height:4px;width:43px;background:var(--teal)}
  .brand{font-family:"Poiret One",sans-serif;color:var(--white);letter-spacing:1px}
  .brand-dot{display:inline-block;width:9px;height:9px;border-radius:50%;background:var(--white);margin-right:6px;vertical-align:middle}
  .kicker{font-family:"Poiret One",sans-serif;font-size:11px;letter-spacing:.5px;color:var(--teal);text-transform:uppercase}
  .headline{font-family:"Poiret One",sans-serif;font-size:23px;letter-spacing:1.5px;text-transform:uppercase;line-height:1}
  .copy{font-size:7px;line-height:10.6px}
  .copy p+p{margin-top:10.6px}
  .badge{position:absolute;border-radius:50%;background:var(--teal);color:var(--white);display:flex;align-items:center;justify-content:center;flex-direction:column;font-family:"Poiret One",sans-serif;text-transform:uppercase}
  .photo{position:absolute}

  /* cover */
  .cover-back{left:51px;top:51px;width:373px;height:373px;background:radial-gradient(ellipse at 50% 30%,#1b1c26 0%,#0a0a0f 55%,#000 100%)}
  .cover-front{left:424px;top:51px;width:373px;height:373px}
  .cover-front .photo{inset:0;background:radial-gradient(circle at 85% 12%,#8fd3ff 0%,#4b6fd6 18%,transparent 45%),radial-gradient(circle at 40% 20%,#6a5ad8 0%,transparent 40%),linear-gradient(180deg,#2c2a8c 0%,#3b1f7a 50%,#1a0e3a 100%)}
  .cover-title{font-family:"Poiret One",sans-serif;color:var(--white);font-size:22px;line-height:21px;letter-spacing:1.5px}
  .cover-year{font-family:"Poiret One",sans-serif;color:var(--white);font-size:38px;letter-spacing:1px}

  /* spread 2 */
  .intro{left:51px;top:431px;width:373px;height:373px;background:var(--teal);color:var(--white)}
  .overview{left:424px;top:431px;width:373px;height:373px;background:var(--white);box-shadow:2px 2px 3px rgba(0,0,0,.15)}
  .event-list{position:absolute;left:58px;top:82px;width:257px;list-style:none}
  .event-list li{height:27.2px;border-bottom:1px solid var(--rule);padding-top:1px}
  .event-date{font-family:"Poiret One",sans-serif;font-size:9.5px;letter-spacing:.3px}
  .event-name{font-size:7px;margin-top:1px}

  /* spread 3 */
  .stage{left:51px;top:812px;width:373px;height:373px;background:var(--black);color:var(--white)}
  .stage .photo{left:171px;top:0;width:202px;height:373px;background:radial-gradient(ellipse at 60% 30%,#b0389a 0%,#5a2a8a 35%,#1d1240 70%,#0d0a1c 100%)}
  .comedy{left:424px;top:812px;width:373px;height:373px;background:var(--white);box-shadow:2px 2px 3px rgba(0,0,0,.15)}
  .comedy .photo{left:138px;top:100px;width:235px;height:273px;background:linear-gradient(160deg,#f2f2f2 0%,#e6d6cc 35%,#2a5fa8 70%,#1f4f8f 100%)}
  .big-title{font-family:"Poiret One",sans-serif;font-size:36px;line-height:34px;letter-spacing:3px;text-transform:uppercase}
  .fact{position:absolute;left:25px;font-family:"Poiret One",sans-serif;font-size:11px;line-height:13px;text-transform:uppercase}
  .fact svg{position:absolute;left:0;top:0}
  .fact span{display:block;padding-left:21px}
  .venue{position:absolute;left:25px;font-size:7px;line-height:9px}
  .venue svg{position:absolute;left:0;top:-1px}
  .venue span{display:block;padding-left:21px}
  .more{position:absolute;left:25px;font-size:5px}
</style>
</head>
<body>

<div class="font-note display">SCHRIFTART: Arbotek Light Rounded <small>(nur 1 Schriftschnitt, sehr dünn)</small></div>

<!-- Cover: back page -->
<section class="panel cover-back">
  <div class="abs brand" style="left:0;width:373px;top:150px;text-align:center;font-size:24px"><span class="brand-dot"></span>Lindenhain</div>
  <div class="abs white" style="left:0;width:373px;top:223px;text-align:center;font-size:7px">www.lindenhain-erleben.de</div>
  <div class="abs kicker" style="left:0;width:373px;top:316px;text-align:center;font-size:11.5px">Wir freuen uns auf Ihren Besuch!</div>
  <div class="abs white" style="left:0;width:373px;top:334px;text-align:center;font-size:7px">Kunst, Kultur und Heimatpflege Lindenhain gGmbH</div>
</section>

<!-- Cover: front page -->
<section class="panel cover-front">
  <div class="photo" role="img" aria-label="Konzertfoto: jubelndes Publikum mit erhobenen Händen unter blauem und violettem Bühnenlicht"></div>
  <div class="abs brand" style="left:27px;top:30px;font-size:18px"><span class="brand-dot"></span>Lindenhain</div>
  <div class="abs white" style="left:27px;top:88px;font-size:6.5px">www.lindenhain-erleben.de</div>
  <div class="abs kicker" style="left:27px;top:161px;font-size:10.5px">Kunst Kultur Genuss Events</div>
  <div class="abs cover-title" style="left:27px;top:178px">Lindenhain<br>Veranstaltungen</div>
  <div class="abs cover-year" style="left:27px;top:218px">2024</div>
  <div class="bar" style="left:28px;top:275px"></div>
</section>

<!-- Intro page -->
<section class="panel intro">
  <div class="abs display" style="left:25px;top:33px;font-size:11px;text-transform:uppercase;letter-spacing:.5px">Lindenhain</div>
  <div class="abs headline" style="left:25px;top:52px">Ausblick 2024</div>
  <div class="abs copy" style="left:58px;top:80px;width:255px">
    <p>Liebe Kunst-, Kultur- und Genuss-Interessierte,</p>
    <p>non eum nusdame praerum quas magnatiasit, nimi, quid eostrum rene provid que liquam, apersperum veliqui buscienisqui velestota susae volorat autem inventiam autatiaest as con esequis eictor adipis volum ut es everro blabo. Arciae cus quos eos erro cone rerum et aut entius modis a volores moluptio. Nemporporem adipsaest estio tem quunt vent peliti aboreium harchil ium res dest, omnim que occat faceperum rehendae. Mus qui ate ligenihilis estrum, optur mos dis es endam, odia sed que nulpa cus.</p>
    <p>Natur? Ihit de dolum, ut es sunt ut qui dendi officiet plisquo cum facit atur, si id maiorrovitas et eum fugia doluptur, idero etur, vendigent latia perro eos as as doluptas int pero comnim essimperio. Et dem que nita quidebit des ima num net quam illabor eptions editibus susandus, sit expe coria quatem de perum re voluptate et prepernam cuptat mi, quatque netur am de voles vent.</p>
    <p>Non eum nusdame praerum quas magnatiasit, nimi, quid eostrum rene provid que liquam, apersperum veliqui buscienisqui velestota susae.</p>
    <p>Ihr Team der Kunst, Kultur und Heimatpflege Lindenhain gGmbH,<br>Harald Wolting, Petra Krings und Nora Vell</p>
  </div>
</section>

<!-- Programme overview -->
<section class="panel overview">
  <div class="abs kicker" style="left:25px;top:33px">Januar | Februar</div>
  <div class="abs headline" style="left:25px;top:52px">Programmübersicht</div>
  <ul class="event-list">
    <li><div class="event-date"><span class="teal">SA 00. JANUAR</span> | 00 UHR | MUSTERPLATZ</div><div class="event-name">Malvina live Blindtext</div></li>
    <li><div class="event-date"><span class="teal">SA 00. JANUAR</span> | 00 UHR | MUSTERPLATZ</div><div class="event-name">Malvina live Blindtext</div></li>
    <li><div class="event-date"><span class="teal">SA 00. JANUAR</span> | 00 UHR | MUSTERPLATZ</div><div class="event-name">Malvina live Blindtext</div></li>
    <li><div class="event-date"><span class="teal">SA 00. JANUAR</span> | 00 UHR | MUSTERPLATZ</div><div class="event-name">Malvina live Blindtext</div></li>
    <li><div class="event-date"><span class="teal">SA 00. JANUAR</span> | 00 UHR | MUSTERPLATZ</div><div class="event-name">Malvina live Blindtext</div></li>
    <li><div class="event-date"><span class="teal">SA 00. JANUAR</span> | 00 UHR | MUSTERPLATZ</div><div class="event-name">Malvina live Blindtext</div></li>
    <li><div class="event-date"><span class="teal">SA 00. JANUAR</span> | 00 UHR | MUSTERPLATZ</div><div class="event-name">Malvina live Blindtext</div></li>
    <li><div class="event-date"><span class="teal">SA 00. JANUAR</span> | 00 UHR | MUSTERPLATZ</div><div class="event-name">Malvina live Blindtext</div></li>
    <li><div class="event-date"><span class="teal">SA 00. JANUAR</span> | 00 UHR | MUSTERPLATZ</div><div class="event-name">Malvina live Blindtext</div></li>
    <li><div class="event-date"><span class="teal">SA 00. JANUAR</span> | 00 UHR | MUSTERPLATZ</div><div class="event-name">Malvina live Blindtext</div></li>
  </ul>
  <div class="badge" style="left:269px;top:261px;width:40px;height:40px"><span style="font-size:6px">Eintritt</span><span style="font-size:13px;line-height:11px">Frei</span></div>
</section>

<!-- Stage event page -->
<section class="panel stage">
  <div class="photo" role="img" aria-label="Foto einer Balletttänzerin in dunklem Kleid, rückwärts gebeugt, vor pink-violettem Nebel"></div>
  <div class="abs kicker" style="left:25px;top:33px">Bühne</div>
  <div class="abs big-title white" style="left:25px;top:50px">Balett</div>
  <div class="badge" style="left:256px;top:24px;width:70px;height:70px;font-size:24px">Neu</div>
  <div class="bar" style="left:25px;top:121px"></div>
  <div class="fact white" style="top:136px">
    <svg width="12" height="12" viewBox="0 0 12 12"><circle cx="6" cy="6" r="5.5" fill="none" stroke="#fff" stroke-width="1"/><rect x="3.2" y="3.5" width="5.6" height="5" fill="none" stroke="#fff" stroke-width=".8"/><line x1="3.2" y1="5" x2="8.8" y2="5" stroke="#fff" stroke-width=".8"/></svg>
    <span>SA 00. Januar</span><span class="teal">00 Uhr</span>
  </div>
  <div class="venue white" style="top:168px">
    <svg width="13" height="13" viewBox="0 0 13 13"><circle cx="6.5" cy="6.5" r="6" fill="none" stroke="#fff" stroke-width="1"/><path d="M6.5 10.2c-1.6-2-2.5-3.3-2.5-4.4a2.5 2.5 0 0 1 5 0c0 1.1-.9 2.4-2.5 4.4z" fill="none" stroke="#fff" stroke-width=".8"/><circle cx="6.5" cy="5.8" r=".8" fill="#fff"/></svg>
    <span>Blindtextschule<br>West</span>
  </div>
  <div class="abs copy" style="left:25px;top:199px;width:130px">Lorem ipsum dolor sit amet, consectetur adipiscing elit. Nulla pulvinar viverra facilisis. Proin fringilla metus dui. Pellentesque est dolor, sagittis quis vulputate fringilla lacinia ligula. Vivamus et, dictum quis turpis. Nulla facilisi. Sed molestie tellus in iaculis laoreet. Maecenas turpis nunc, suscipit nec nisl eu, fringilla lacinia ligula. Vivamus pulvinar egestas arcu fermentum fermentum. Etiam faucibus!</div>
  <div class="more white" style="top:342px">Mehr Infos: www.fuelltextstube.de</div>
</section>

<!-- Comedy event page -->
<section class="panel comedy">
  <div class="photo" role="img" aria-label="Freigestelltes Foto eines Komikers im blauen Poloshirt, der lachend einen orangefarbenen Föhn hält"></div>
  <div class="abs kicker" style="left:25px;top:33px">Comedy</div>
  <div class="abs big-title" style="left:25px;top:50px;color:var(--ink)">Max<br>Muster</div>
  <div class="badge" style="left:218px;top:24px;width:70px;height:70px;font-size:24px">Tipp</div>
  <div class="bar" style="left:25px;top:121px"></div>
  <div class="fact" style="top:136px">
    <svg width="12" height="12" viewBox="0 0 12 12"><circle cx="6" cy="6" r="6" fill="#111"/><rect x="3.2" y="3.5" width="5.6" height="5" fill="none" stroke="#fff" stroke-width=".8"/><line x1="3.2" y1="5" x2="8.8" y2="5" stroke="#fff" stroke-width=".8"/></svg>
    <span>SA 00. Januar</span><span class="teal">00 Uhr</span>
  </div>
  <div class="venue" style="top:168px">
    <svg width="13" height="13" viewBox="0 0 13 13"><circle cx="6.5" cy="6.5" r="6.5" fill="#111"/><path d="M6.5 10.2c-1.6-2-2.5-3.3-2.5-4.4a2.5 2.5 0 0 1 5 0c0 1.1-.9 2.4-2.5 4.4z" fill="#fff"/><circle cx="6.5" cy="5.8" r=".8" fill="#111"/></svg>
    <span>Blindtextschule West</span>
  </div>
  <div class="abs copy" style="left:25px;top:199px;width:130px">Lorem ipsum dolor sit amet, consectetur adipiscing elit. Nulla pulvinar viverra facilisis. Proin fringilla metus dui. Pellentesque est dolor, sagittis quis vulputate fringilla lacinia ligula. Vivamus et, dictum quis turpis. Nulla facilisi. Sed molestie tellus in iaculis laoreet. Maecenas turpis nunc, suscipit nec nisl eu, fringilla lacinia ligula. Vivamus pulvinar egestas arcu fermentum fermentum. Etiam faucibus!</div>
  <div class="more" style="top:342px">Mehr Infos: www.fuelltextstube.de</div>
</section>

</body>
</html>
```